Design a double sided business card

We are looking for a clean, eye-catching, and contemporary design that enhances the brand and presents a premium, professional image. Our preference is for a brown card with black gloss detailing and embossed elements; however, we are open to creative input and design suggestions that best achieve a strong visual impact.

Please see the attached existing business card for reference. We use both black and brown colours consistently across our branding.

On sample provided

```html
<!DOCTYPE html>
<html lang="en">
<head>
<meta charset="utf-8">
<title>Halden – Business Card</title>
<link rel="stylesheet" href="https://fonts.googleapis.com/css2?family=Montserrat:wght@500;600;700&family=Poppins:wght@400;500&display=swap">
<style>
  :root {
    --backdrop: #6a6a6c;
    --ink: #141414;
    --card-black: #0f0f0f;
    --tan: #d7c2a8;
    --tan-light: #decbb4;
    --tan-deep: #cdb698;
    --gold-text: #dcc7ad;
  }
  * { margin: 0; padding: 0; box-sizing: border-box; }
  html, body { width: 900px; height: 1200px; overflow: hidden; }
  body { background: var(--backdrop); position: relative; font-family: "Poppins", sans-serif; }

  .card { position: absolute; left: 150px; width: 602px; height: 387px; overflow: hidden; }
  .card--front { top: 168px; background: var(--card-black); }
  .card--back { top: 644px; background: linear-gradient(135deg, var(--tan-deep), var(--tan-light) 55%, var(--tan)); }

  /* front */
  .front-texture { position: absolute; inset: 0; width: 100%; height: 100%; }
  .front-band { position: absolute; left: 0; right: 0; top: 150px; height: 84px; background: var(--card-black); }
  .front-mark { position: absolute; left: 72px; top: 160px; width: 64px; height: 64px; background: var(--gold-text); }
  .front-name {
    position: absolute; left: 168px; top: 160px; line-height: 64px;
    font-family: "Montserrat", sans-serif; font-weight: 700; font-size: 50px;
    letter-spacing: 7px; color: var(--gold-text);
  }

  /* back */
  .back-mark { position: absolute; left: 135px; top: 118px; width: 90px; height: 90px; background: var(--ink); }
  .back-name {
    position: absolute; left: 44px; width: 272px; top: 236px; text-align: center;
    font-family: "Montserrat", sans-serif; font-weight: 700; font-size: 32px;
    letter-spacing: 5px; color: var(--ink);
  }
  .divider { position: absolute; left: 324px; top: 94px; width: 2px; height: 201px; background: var(--ink); }
  .contact { position: absolute; left: 345px; top: 92px; color: var(--ink); }
  .contact__name { font-family: "Montserrat", sans-serif; font-weight: 700; font-size: 22px; line-height: 26px; letter-spacing: .3px; }
  .contact__role { font-family: "Montserrat", sans-serif; font-weight: 500; font-size: 13.5px; letter-spacing: 1px; margin-top: 2px; }
  .contact__address { font-size: 14px; line-height: 23px; margin-top: 12px; letter-spacing: .4px; }
  .contact__list { list-style: none; margin-top: 9px; font-size: 14.5px; letter-spacing: .9px; }
  .contact__list li { display: flex; align-items: center; gap: 5px; height: 24px; }
  .contact__list svg { width: 11px; height: 11px; flex: none; }
</style>
</head>
<body>

<section class="card card--front" aria-label="Card front">
  <svg class="front-texture" role="img" aria-label="Embossed repeating brand pattern on black card stock" viewBox="0 0 602 387" preserveAspectRatio="none">
    <defs>
      <linearGradient id="frontShade" x1="0" y1="0" x2="1" y2="0">
        <stop offset="0" stop-color="#121212"/>
        <stop offset="0.6" stop-color="#1b1b1b"/>
        <stop offset="1" stop-color="#3a3a3b"/>
      </linearGradient>
    </defs>
    <rect width="602" height="387" fill="url(#frontShade)"/>
  </svg>
  <div class="front-band"></div>
  <div class="front-mark"></div>
  <div class="front-name">HALDEN</div>
</section>

<section class="card card--back" aria-label="Card back">
  <div class="back-mark"></div>
  <div class="back-name">HALDEN</div>
  <div class="divider"></div>
  <div class="contact">
    <h1 class="contact__name">RAVI MEHTA</h1>
    <p class="contact__role">DIRECTOR</p>
    <p class="contact__address">The Orchard Mill Lane<br>Eastbridge EB4 2QT</p>
    <ul class="contact__list">
      <li><svg viewBox="0 0 24 24"><path fill="#141414" d="M6.6 10.8a15.1 15.1 0 0 0 6.6 6.6l2.2-2.2a1 1 0 0 1 1-.25 11.4 11.4 0 0 0 3.6.57 1 1 0 0 1 1 1V20a1 1 0 0 1-1 1A17 17 0 0 1 3 4a1 1 0 0 1 1-1h3.5a1 1 0 0 1 1 1c0 1.25.2 2.45.57 3.57a1 1 0 0 1-.25 1z"/></svg>0800 555 0142</li>
      <li><svg viewBox="0 0 24 24"><rect x="6" y="1.5" width="12" height="21" rx="2" fill="none" stroke="#141414" stroke-width="2.4"/><circle cx="12" cy="18.5" r="1.3" fill="#141414"/></svg>07700900316</li>
      <li><svg viewBox="0 0 24 24"><rect x="2" y="5" width="20" height="14" fill="#141414"/><path d="M2 5l10 8 10-8" fill="none" stroke="#d7c2a8" stroke-width="1.8"/></svg>ravi@halden.co.uk</li>
      <li><svg viewBox="0 0 24 24" fill="none" stroke="#141414" stroke-width="2"><circle cx="12" cy="12" r="10"/><ellipse cx="12" cy="12" rx="4.5" ry="10"/><path d="M2 12h20M4 7h16M4 17h16"/></svg>www.halden.co.uk</li>
    </ul>
  </div>
</section>

</body>
</html>
```